1) This is a self-help business book for women executives and entrepreneurs that will assist women in getting to the next level of success. The reader should feel confident that this book will solve their problem in elevating their current position.
2) The primary message I want to convey on the cover is that they are in the right hands to solve their issue of promoting themselves, without losing themselves or the ones they love. Women can have it all!
3) Can be a realistic sketch of: I envision a woman sitting on a Queen Anne white chair (victorian style tufted in diamonds) with dark brown / reddish highlights in hair. She has almond/light brown skin.
She is dressed professionally - see attached pic in red dress - change to navy blue dress w/ solid nude pumps. Her hand is out holding a diamond paperweight. The light beam hits the bottom of the paperweight and fractures out to gold and silver sparkles (like 3D sparkles). The 4 corners of the book cover to include gold and silver matte damask.
Like purple title in a font with curves. Preferred book colors: white, gold, silver, purple
4) The setting of the book in a modern and current day for executive women.
5) Book Title -- The Velvet Compass
Subtitle -- Chart Fresh Paths while Keeping Every Morning Bright for Kin
6) Author -- Dr. Lorna Pettigrew
7) ebook size - 4 1/2 x 7 1/2, cover 7.3, not more than 50Mb, 2560x 1600 jpg
8) See attached example of Queen Anne white Chair tufted w/ diamonds and flap copy book description
9) see attached example of diamond refracting light (not rainbow - gold / silver )
Idea 2 -----
Woman hand holding diamond paperweight; can see glimmer of facets within diamond;singular white light towards one side of diamond and the other side refracts with gold / silver glistens (see pic - not rainbow as an pic)

```html
<!DOCTYPE html>
<html lang="en">
<head>
<meta charset="utf-8">
<title>The Velvet Compass — Book Cover</title>
<link rel="stylesheet" href="https://fonts.googleapis.com/css2?family=Josefin+Sans:wght@100;300;400&family=Montserrat:wght@400;600;700;800&display=swap">
<style>
  :root {
    --stage: #efefef;
    --cover-black: #0c0c0c;
    --cover-charcoal: #2a2a2a;
    --ink-white: #ffffff;
    --ink-soft: #d8d8d8;
    --ink-muted: #8a8a8a;
    --gold: #c9b27a;
    --gold-light: #dcc99a;
    --gold-deep: #a88f55;
    --author-ink: #111111;
    --photo-warm: #6b4d3c;
    --photo-glow: #a88a76;
    --photo-blue: #1f4fa8;
  }
  * { box-sizing: border-box; margin: 0; padding: 0; }
  html, body {
    width: 1200px;
    height: 800px;
    overflow: hidden;
    background: var(--stage);
  }
  .stage {
    position: relative;
    width: 1200px;
    height: 800px;
  }

  /* ---------- Back cover ---------- */
  .back-cover {
    position: absolute;
    left: 230px;
    top: 130px;
    width: 360px;
    height: 540px;
    background: linear-gradient(180deg, var(--cover-black) 0%, var(--cover-charcoal) 100%);
    color: var(--ink-soft);
    font-family: "Montserrat", sans-serif;
    padding: 120px 40px 0 40px;
  }
  .back-cover .blurb {
    font-size: 8.5px;
    line-height: 1.6;
    margin-bottom: 14px;
  }
  .back-cover .back-heading {
    font-weight: 800;
    font-size: 10px;
    letter-spacing: 0.06em;
    color: var(--ink-white);
    text-align: center;
    margin: 18px 0 16px;
  }
  .back-cover .site-label {
    font-weight: 700;
    font-size: 8px;
    letter-spacing: 0.06em;
    color: var(--ink-white);
    text-align: center;
    line-height: 1.5;
    margin-top: 14px;
  }
  .back-cover .site-url {
    font-size: 7.5px;
    letter-spacing: 0.1em;
    color: var(--ink-muted);
    text-align: center;
    margin-top: 16px;
    text-transform: uppercase;
  }

  /* ---------- Front cover ---------- */
  .front-cover {
    position: absolute;
    left: 610px;
    top: 130px;
    width: 360px;
    height: 540px;
    overflow: hidden;
    background: var(--cover-black);
  }
  .cover-photo {
    position: absolute;
    left: 0;
    top: 0;
    width: 100%;
    height: 100%;
    background:
      radial-gradient(ellipse 55% 45% at 72% 62%, var(--photo-glow) 0%, rgba(168,138,118,0) 70%),
      radial-gradient(ellipse 60% 30% at 80% 100%, var(--photo-blue) 0%, rgba(31,79,168,0) 75%),
      linear-gradient(180deg, var(--cover-black) 0%, #1a1411 26%, var(--photo-warm) 55%, #4a3326 80%, #2a2140 100%);
  }
  .title-block {
    position: absolute;
    top: 26px;
    left: 0;
    width: 100%;
    text-align: center;
    color: var(--ink-white);
    font-family: "Josefin Sans", sans-serif;
  }
  .title-small {
    font-weight: 300;
    font-size: 30px;
    letter-spacing: 0.02em;
    line-height: 1;
    padding-left: 10px;
  }
  .title-large {
    font-weight: 100;
    font-size: 66px;
    letter-spacing: 0.01em;
    line-height: 1;
    margin-top: 2px;
    padding-left: 26px;
  }
  .subtitle {
    margin-top: 8px;
    font-family: "Montserrat", sans-serif;
    font-weight: 400;
    font-size: 7.5px;
    letter-spacing: 0.08em;
    line-height: 1.35;
    color: var(--gold);
    text-transform: uppercase;
  }
  .author-band {
    position: absolute;
    left: 0;
    top: 456px;
    width: 100%;
    height: 34px;
    background: linear-gradient(90deg, var(--gold-deep) 0%, var(--gold-light) 45%, var(--gold) 100%);
    display: flex;
    align-items: center;
    justify-content: center;
  }
  .author-name {
    font-family: "Montserrat", sans-serif;
    font-weight: 800;
    font-size: 17px;
    letter-spacing: 0.03em;
    color: var(--author-ink);
    text-transform: uppercase;
  }
</style>
</head>
<body>
<main class="stage">

  <section class="back-cover" aria-label="Back cover">
    <p class="blurb">Every leader reaches a moment when the next step feels uncertain. This book offers a steady hand, practical tools and honest stories for that climb.</p>
    <p class="blurb">Learn to speak about your work with clarity, ask for what you have earned and keep your home life whole while you grow.</p>
    <p class="blurb">Drawing on years of coaching women in business, the author shares simple habits that turn quiet talent into visible results, without losing the people and values that matter most.</p>
    <p class="back-heading">YOUR NEXT LEVEL STARTS HERE</p>
    <p class="blurb">Chart your own course with confidence, and bring everyone you love along for the journey.</p>
    <p class="site-label">VISIT THE AUTHORS<br>WEBSITE AT:</p>
    <p class="site-url">www.velvetcompassbook.com</p>
  </section>

  <section class="front-cover" aria-label="Front cover">
    <div class="cover-photo" role="img" aria-label="Photograph of the smiling author in a royal blue top, holding up a sparkling diamond that catches a beam of light, against a glittering bronze sequin backdrop"></div>

    <header class="title-block">
      <h1>
        <span class="title-small" style="display:block">THE VELVET</span>
        <span class="title-large" style="display:block">COMPASS</span>
      </h1>
      <p class="subtitle">Chart fresh paths while<br>keeping every morning bright for kin</p>
    </header>

    <div class="author-band">
      <p class="author-name">Dr. Lorna Pettigrew</p>
    </div>
  </section>

</main>
</body>
</html>
```